Medical Learning Web Design Project

The web site will be a site for medical students. It is aimed at providing a collaborative place for students to study, learn, question each other and challenge each other with learning. The site needs to have a section on the page that is for the content and this needs to be relatively clean and clinical. The surrounding elements will be informative (for the statistics, challenge etc). There will also be a slide-out screen that allows for the social/friend elements of the site.

The colour scheme needs to be clean and clinical where appropriate, but also engaging and exciting for the social/competitive elements.
Updates

Just for clarity: The site isn't expected to be 'coded' ... it is just the layered PSD files that I need.

Also, with regards to the navigation buttons ... they will never ALL be present at the same time so don't feel the need to design all on one page, but creativity around allowing few or many on a page will be an advantage ...

Thanks

Hi,

Please note that the image uploaded has been done as a wireframe by the developers. I am looking for a more creative and engaging way of presenting that content ...

Thanks

Hi all

Thank you all for the designs so far ...!

Please have a look at the new uploaded file, I am also looking not just for a 'templated home page' but also some different layouts that are represented in these wireframes. If the various layouts represented can be condensed down into 1 or 2 page templates with appropriate colour schemes to capture the type of content on the page (as already mentioned ... social .. competitive ... learning), then that will help me live the concepts better too! The friends tab for instance I have envisaged as a slider covering the screen and then sliding back when complete ... but let me see what creativity you can give to this ...!

Many thanks

Target Market(s)

Medical Students

Industry/Entity Type

Medical

Requirements
Must have
• - Not cluttered appearance
- Dynamic navigation (ie. site will be developed to only show relevant navigation buttons on each page ...)
- Navigation buttons (need to be individual buttons) will be: 'Home', 'Take the tour', 'What your peers say', 'Subscriptions', 'Free Signup', 'Contact us', 'Moderation', 'Statistics', 'Competition', 'Answer Questions', 'Post Questions', 'My profile', 'Friends'
- Please also ensure it is engaging for social elements and competitive elements (perhaps slightly different design for pages focussed on each element)
- Please also ensure that there is a masculine design and feminine design that has continuity for the site but depending on gender the design can be tailored to be more appealing (that means perhaps male social design, male competitive design, female social design, female competitive design ... without loosing continuity through the site).
- Photoshop PSD format
- Pixel perfect at least 1000 pixels wide (but the design needs to allow for various monitor sizes (only desktop or laptops ... not tablets or smart phones)

```html
<!DOCTYPE html>
<html lang="en">
<head>
<meta charset="utf-8">
<title>Clinova – The Medical Peer Review</title>
<link href="https://fonts.googleapis.com/css2?family=Gochi+Hand&family=PT+Sans:ital,wght@0,400;0,700;1,400&family=PT+Sans+Narrow&display=swap" rel="stylesheet">
<style>
:root{
  --header:#2d4652;
  --orange:#f39322;
  --page:#f2f2f2;
  --panel:#ffffff;
  --border:#dcdcdc;
  --text:#333333;
  --muted:#666666;
  --sky:#33c6f4;
  --bullet:#b8561e;
}
*{box-sizing:border-box;margin:0;padding:0}
html,body{width:1200px;height:879px;overflow:hidden}
body{background:var(--page);font-family:"PT Sans",sans-serif;color:var(--text);position:relative;font-size:12px}
.abs{position:absolute}
.site-header{position:absolute;left:0;top:0;width:1200px;height:106px;background:var(--header)}
.brand{left:166px;top:14px;font-family:"Gochi Hand",cursive;font-size:46px;color:var(--orange);line-height:1}
.brand-tag{left:167px;top:63px;color:#fff;font-size:13px}
.quote{left:343px;top:33px;color:#fff;font-style:italic;font-size:12px;line-height:19px}
.quote span{display:block;padding-left:60px}
.web-links{left:771px;top:12px;color:#fff;font-style:italic;font-size:12px;display:flex;align-items:center;gap:3px}
.web-links .sq{width:15px;height:15px;border-radius:3px;display:inline-block}
.web-links em{margin-right:9px}
.login input{position:absolute;top:48px;height:25px;border:0;background:#fff;font:12px "PT Sans",sans-serif;color:#555;padding:0 7px}
.login .btn{position:absolute;left:971px;top:48px;width:63px;height:25px;background:var(--orange);color:#2d4652;font:15px "PT Sans Narrow",sans-serif;text-align:center;line-height:25px}
.login .keep{position:absolute;left:707px;top:82px;color:#fff;font-style:italic;font-size:12px;display:flex;align-items:center;gap:9px}
.keep i{width:14px;height:14px;background:#fff;display:inline-block}
.login .forgot{position:absolute;left:839px;top:83px;color:#fff;font-style:italic;font-size:12px;text-decoration:underline}
.main-nav{position:absolute;left:0;top:106px;width:1200px;height:34px;background:linear-gradient(#f7f7f7,#d6d6d6)}
.main-nav ul{list-style:none;display:flex;position:absolute;left:154px;width:892px;height:34px;border-top:2px solid #24363f}
.main-nav li{flex:1;text-align:center;font:15px/32px "PT Sans Narrow",sans-serif;color:#2d3e47;border-right:1px solid #c6c6c6}
.main-nav li:last-child{border-right:0;flex:1.6}
.news{left:162px;top:150px;width:628px;height:28px;background:#fff;border:1px solid var(--border);padding:0 10px;line-height:26px;font-size:12px}
.share{top:155px;display:flex;align-items:center;gap:8px;font-size:11px;color:#6a7fae}
.share b{font-weight:400;border:1px solid #c7cfe0;background:#eef1f8;color:#3b5998;padding:1px 5px;border-radius:2px}
.panel{position:absolute;background:var(--panel);border:1px solid var(--border)}
.slider{left:162px;top:186px;width:873px;height:300px}
.hand{font-family:"Gochi Hand",cursive;color:#243a46}
.slider h1{position:absolute;left:61px;top:40px;font-size:22px;font-weight:400;letter-spacing:.5px}
.features{position:absolute;left:66px;top:75px;list-style:none}
.features li{font-size:12px;height:27.7px;padding-left:20px;position:relative}
.features li:before{content:"";position:absolute;left:2px;top:4px;border-left:4px solid var(--bullet);border-top:3px solid transparent;border-bottom:3px solid transparent}
.photo{position:absolute}
.arrow{position:absolute;top:136px}
.works{left:162px;top:496px;width:356px;height:273px}
.works h2{position:absolute;left:15px;top:10px;font-size:22px;font-weight:400}
.video{position:absolute;left:15px;top:46px;width:340px;height:191px;background:linear-gradient(#cfd8dc,#eef1f2);border:2px solid #444}
.player-bar{position:absolute;left:15px;top:238px;width:340px;height:14px;background:linear-gradient(#e8e8e8,#bcbcbc);font-size:7px;line-height:14px}
.feed{left:540px;top:496px;width:232px;height:273px}
.feed .title{position:absolute;left:10px;top:11px;font-size:12px;line-height:17px}
.feed .box{position:absolute;left:10px;top:55px;width:211px;height:166px;background:var(--sky);color:#fff;padding:16px 13px 0;font-size:11px;line-height:17px}
.box .date{margin:4px 0 14px;padding-bottom:10px;border-bottom:1px solid #7bd9f7}
.box .date:last-child{border:0}
.follow{position:absolute;left:12px;top:228px;color:var(--sky);font-weight:700;line-height:1}
.follow small{font-size:8px;display:block}
.follow span{font-size:22px}
.social{left:784px;top:496px;width:252px;height:273px}
.social .head{position:absolute;left:19px;top:12px;font-size:12px;line-height:20px}
.social .head b{font-weight:400;border:1px solid #c7cfe0;background:#eef1f8;color:#3b5998;padding:0 5px;font-size:10px;margin-right:3px}
.social hr{position:absolute;left:14px;top:60px;width:224px;border:0;border-top:1px solid #ddd}
.social .count{position:absolute;left:22px;top:85px;font-size:11px}
.fans{position:absolute;left:22px;top:101px;display:grid;grid-template-columns:repeat(4,46px);gap:6px 5px;font-size:8px;color:#777;text-align:center}
.fans div div{width:46px;height:46px;margin-bottom:3px}
.footer-links{left:0;width:1200px;top:804px;text-align:center;font-size:11px}
.copy{left:0;width:1200px;top:824px;text-align:center;font-size:11px}
</style>
</head>
<body>
<header class="site-header">
  <div class="abs brand">Clinova</div>
  <div class="abs brand-tag">The medical Peer Review</div>
  <p class="abs quote">"Clinova keeps me ahead of the game, testing my knowledge..."<span>--Tom, doctor in training, Northfield university</span></p>
  <div class="abs web-links"><em>Clinova on the web</em>
    <i class="sq" style="background:#4a6aa8"></i><i class="sq" style="background:#f08a24"></i><i class="sq" style="background:#3fb6e8"></i><i class="sq" style="background:#2d7bb5"></i><i class="sq" style="background:#f57c1f"></i><i class="sq" style="background:#e6e6e6"></i><i class="sq" style="background:#3b9a3e"></i><i class="sq" style="background:#cc2127"></i>
  </div>
  <form class="login">
    <input style="left:707px;width:127px" value="User Name">
    <input style="left:839px;width:127px" value="Password">
    <div class="btn">LOGIN</div>
    <label class="keep"><i></i>keep me Signed in</label>
    <span class="forgot">Forgot your password</span>
  </form>
</header>
<nav class="main-nav"><ul>
  <li>Home</li><li>Take The Tour</li><li>What your peers say</li><li>Subscription Plans</li><li>Free Signup</li><li>Contact Us</li>
</ul></nav>

<div class="abs news">about 2 days ago : Clinova is now on Circlebook. Follow Us here</div>
<div class="abs share" style="left:806px"><b>Like</b>1</div>
<div class="abs share" style="left:871px"><b style="background:#3d6fc7;color:#fff;border-color:#3d6fc7">+1</b>200</div>
<div class="abs share" style="left:939px;color:#33b5e5"><b style="background:#e6f5fc;color:#2a9ad0;border-color:#cfe9f5">Share</b>7,231</div>

<section class="panel slider">
  <svg class="arrow" style="left:11px" width="18" height="30" viewBox="0 0 18 30"><path d="M15 3 4 15l11 12" fill="none" stroke="#222" stroke-width="4"/></svg>
  <svg class="arrow" style="left:838px" width="18" height="30" viewBox="0 0 18 30"><path d="M3 3l11 12L3 27" fill="none" stroke="#222" stroke-width="4"/></svg>
  <h1 class="hand">Clinova - The Medical Peer Review</h1>
  <ul class="features">
    <li>Test your medical knowledge</li>
    <li>Answer a vast array of medical questions</li>
    <li>Earn trophies as your knowledge increases</li>
    <li>Rate questions from peers</li>
    <li>Ask your own questions</li>
    <li>Link to your friends and check their progress</li>
    <li>29.903 Questions answered!</li>
  </ul>
  <div class="photo" role="img" aria-label="Group of medical staff in scrubs and white coats" style="left:405px;top:21px;width:203px;height:125px;background:linear-gradient(135deg,#5b8fc9,#d9e4ef);border:1px solid #bbb"></div>
  <div class="photo" role="img" aria-label="Students practising on a patient in a clinic" style="left:617px;top:21px;width:201px;height:124px;background:linear-gradient(135deg,#8e9aa3,#e3e6e8)"></div>
  <div class="photo" role="img" aria-label="Researcher using a pipette in a laboratory" style="left:405px;top:152px;width:201px;height:124px;background:linear-gradient(135deg,#6d5a4e,#e6e2dc)"></div>
  <div class="photo" role="img" aria-label="Scientist in safety glasses examining a test tube" style="left:617px;top:152px;width:201px;height:124px;background:linear-gradient(135deg,#bfcbd6,#f1f4f7)"></div>
</section>

<section class="panel works">
  <h2 class="hand">How Clinova Works</h2>
  <div class="video" role="img" aria-label="Video still of smiling medical students in white coats">
    <svg style="position:absolute;left:152px;top:73px" width="44" height="44" viewBox="0 0 44 44"><circle cx="22" cy="22" r="21" fill="#e05a5a" opacity=".75"/><path d="M17 13v18l14-9z" fill="#b84444"/></svg>
  </div>
  <div class="player-bar">
    <svg style="position:absolute;left:6px;top:3px" width="8" height="8"><path d="M0 0v8l7-4z" fill="#333"/></svg>
    <span style="position:absolute;left:30px;top:5px;width:160px;height:3px;background:#888"></span>
    <span style="position:absolute;left:212px">0:00 / 1:33</span>
  </div>
</section>

<section class="panel feed">
  <p class="title">Clinova Medical Peer Review<br>Clinova</p>
  <div class="box">
    <p>Lorem Ipsum is simply dummy text of the printing and typesetting industry</p><p class="date">28.12.2012</p>
    <p>Lorem Ipsum is simply dummy text of the printing and typesetting industry</p><p class="date">28.12.2012</p>
  </div>
  <div class="follow"><small>FOLLOW US ON</small><span>Chirper</span></div>
</section>

<section class="panel social">
  <p class="head">Clinova on Circlebook<br><b>Like</b> you like this</p>
  <hr>
  <p class="count">5,019 people like <strong>Clinova Study Hub</strong>.</p>
  <div class="fans">
    <div><div role="img" aria-label="Profile photo" style="background:#6e7a5c"></div>Callum</div>
    <div><div role="img" aria-label="Default profile silhouette" style="background:#c9d3e4"></div>Gita</div>
    <div><div role="img" aria-label="Profile photo" style="background:#7a4a32"></div>Greta</div>
    <div><div role="img" aria-label="Profile photo" style="background:#5a3b2c"></div>Elena</div>
    <div><div role="img" aria-label="Default profile silhouette" style="background:#c9d3e4"></div>Dev</div>
    <div><div role="img" aria-label="Profile photo" style="background:#9c8c7a"></div>Kira</div>
    <div><div role="img" aria-label="Bouquet of red roses" style="background:#b8262d"></div>Amal</div>
    <div><div role="img" aria-label="Profile photo" style="background:#a39070"></div>Sonia</div>
  </div>
</section>

<p class="abs footer-links">Home &nbsp;|&nbsp; Take the tour &nbsp;|&nbsp; What your peers say &nbsp;|&nbsp; Subscription Plans &nbsp;|&nbsp; Free Signup &nbsp;|&nbsp; Contact us &nbsp;|&nbsp; Sitemap</p>
<p class="abs copy">Copyrights @ 2012 All Rights Reserved</p>
</body>
</html>
```